Veltrano - Mechanic/Collision Center Business Card

We're looking for a business card design for our mechanic/ collision repair shop.

Can be with colours or monochromatic.

See the attached files.

Many thanks

```html
<!DOCTYPE html>
<html lang="pt">
<head>
<meta charset="utf-8">
<title>Veltrano – Business Card</title>
<link rel="stylesheet" href="https://fonts.googleapis.com/css2?family=Open+Sans:wght@400;700;800&display=swap">
<style>
  :root {
    --page-bg: #e9e9e7;
    --card-white: #f6f6f6;
    --card-dark: #1a1d20;
    --brand-blue: #1b9bd7;
    --ink: #1c1c1c;
    --rule: #111111;
  }
  * { margin: 0; padding: 0; box-sizing: border-box; }
  html, body { width: 1200px; height: 900px; overflow: hidden; }
  body {
    background: var(--page-bg);
    font-family: "Open Sans", Arial, sans-serif;
    display: flex;
    flex-direction: column;
    align-items: center;
    justify-content: center;
    gap: 40px;
  }
  .card {
    position: relative;
    width: 700px;
    height: 390px;
    border: 3px solid var(--brand-blue);
    overflow: hidden;
  }
  /* Back side */
  .card--back {
    background: var(--card-dark);
    display: flex;
    align-items: center;
    justify-content: center;
  }
  .wordmark {
    display: flex;
    align-items: center;
    gap: 16px;
    font-weight: 800;
    letter-spacing: 2px;
    text-transform: uppercase;
  }
  .wordmark__dot {
    width: 22px; height: 22px; border-radius: 50%;
  }
  .card--back .wordmark { color: #ffffff; font-size: 58px; }
  .card--back .wordmark__dot { background: #ffffff; width: 30px; height: 30px; }

  /* Front side */
  .card--front { background: var(--card-white); }
  .front__brand {
    position: absolute;
    left: 0; top: 0;
    width: 365px; height: 290px;
    display: flex; align-items: center; justify-content: center;
  }
  .card--front .wordmark { color: var(--ink); font-size: 40px; }
  .card--front .wordmark__dot { background: var(--brand-blue); }
  .front__divider {
    position: absolute;
    left: 365px; top: 34px;
    width: 2px; height: 256px;
    background: var(--rule);
  }
  .contact {
    position: absolute;
    left: 390px; top: 26px;
    color: var(--ink);
    font-size: 16.5px;
    line-height: 24px;
  }
  .contact__name {
    color: var(--brand-blue);
    font-size: 25px;
    font-weight: 800;
    line-height: 30px;
  }
  .contact__role { margin-bottom: 0; }
  .contact__company { margin-top: 22px; }
  .contact__line { white-space: nowrap; }
  .front__wave {
    position: absolute;
    left: 0; top: 0;
    width: 100%; height: 100%;
  }
</style>
</head>
<body>
  <section class="card card--back" aria-label="Card back">
    <div class="wordmark">
      <span class="wordmark__dot"></span>
      <span class="wordmark__name">Veltrano</span>
    </div>
  </section>

  <section class="card card--front" aria-label="Card front">
    <svg class="front__wave" viewBox="0 0 694 384" preserveAspectRatio="none" aria-hidden="true">
      <path d="M0,292 C180,278 330,298 460,332 C560,358 640,360 694,352 L694,384 L0,384 Z" fill="#1b9bd7"/>
      <path d="M0,310 C180,296 330,316 460,350 C560,376 640,378 694,370" fill="none" stroke="#f6f6f6" stroke-width="14"/>
      <path d="M0,301 C180,287 330,307 460,341 C560,367 640,369 694,361" fill="none" stroke="#111111" stroke-width="3"/>
    </svg>

    <div class="front__brand">
      <div class="wordmark">
        <span class="wordmark__dot"></span>
        <span class="wordmark__name">Veltrano</span>
      </div>
    </div>

    <div class="front__divider"></div>

    <div class="contact">
      <div class="contact__name">Tiago Moreira</div>
      <div class="contact__role">manager</div>
      <div class="contact__line">+351 910 000 482</div>
      <div class="contact__line contact__company">Veltrano, LDA</div>
      <div class="contact__line">Rua das Oficinas, 14</div>
      <div class="contact__line">4400-120 Vila Nova</div>
      <div class="contact__line">+351 220 000 731</div>
      <div class="contact__line">geral@veltrano.pt</div>
      <div class="contact__line">www.veltrano.pt/oficina</div>
    </div>
  </section>
</body>
</html>
```